Website design for new health & wellness company

We need our website to be designed in a user friendly way. Needs to be aesthetically pleasing to viewer and easy to navigate and upload content for our small team . The logo should be completely redesigned , please do not reference the current one thats on our site for a starting place. (included below though) We want to move away from that.

the website is : www.brightpathmoments.net

We are a small group of writers/coaches who believe that to change the world you have to be the change and we provide tips/suggestions for every day life that if followed can make a huge difference in your life and overall being.

Target Market(s)

Men and women ages 22 to 50

Industry/Entity Type

Health And Wellness

Logo Text

Cultivate the life of your dreams

Coding

Coded - Design and coding required

Number of Pages Required

3 page

Font styles to use
Sans Serif

Colors

Designer to choose colors to be used in the design.

Requirements
Must have
• Easy to navigate. Mobile friendly. Gender neutral, should appeal to both.

```html
<!DOCTYPE html>
<html lang="en">
<head>
<meta charset="utf-8">
<title>BrightPath – Health &amp; Wellness</title>
<link href="https://fonts.googleapis.com/css2?family=Raleway:wght@400;500;600;700;800&family=Open+Sans:wght@400;600;700&display=swap" rel="stylesheet">
<style>
:root{
  --green:#8cc63e;
  --green-dark:#79b22f;
  --teal:#19b2c3;
  --orange:#fb8540;
  --navy:#2e3a4f;
  --ink:#2b2b2b;
  --muted:#6f6f6f;
  --line:#e3e3e3;
  --white:#ffffff;
}
*{margin:0;padding:0;box-sizing:border-box}
html,body{width:1200px;height:4054px;overflow:hidden;background:var(--white)}
body{position:relative;font-family:"Open Sans",Arial,sans-serif;color:var(--ink)}
.abs{position:absolute}

/* hero */
.hero{left:0;top:0;width:1200px;height:700px;
  background:
    linear-gradient(180deg,rgba(0,0,0,0) 55%,rgba(70,50,40,.35) 100%),
    linear-gradient(100deg,#6a5648 0%,#8d7867 32%,#b9a898 55%,#ddd2c6 75%,#eae3da 100%)}
.topbar{left:0;top:0;width:1200px;height:22px;background:rgba(20,20,20,.55);color:#ddd;font-size:9px;line-height:22px}
.topbar .links{left:158px}
.topbar .links span{margin-right:18px}
.topbar .social{right:82px;top:6px;display:flex;gap:10px}
.topbar .social i{display:block;width:10px;height:10px;border-radius:50%;background:#cfcfcf}

.header{left:81px;top:27px;width:1038px;height:141px;background:var(--white);box-shadow:0 2px 8px rgba(0,0,0,.12)}
.logo{left:22px;top:48px;display:flex;align-items:center;gap:10px;font-family:"Raleway",sans-serif;font-weight:800;font-size:38px;color:var(--green);letter-spacing:1px}
.logo i{display:block;width:16px;height:16px;background:var(--green)}
.contact-item{top:30px;display:flex;gap:9px;align-items:flex-start;font-size:11px;line-height:15px}
.contact-item svg{width:20px;height:20px;margin-top:3px}
.contact-item small{display:block;color:var(--muted);font-size:10px}
.contact-item b{font-weight:600;font-size:11px}
.nav{right:16px;top:116px;display:flex;gap:28px;font-size:15px;color:#333}

.hero-title{left:113px;top:248px;color:var(--white);font-family:"Raleway",sans-serif;font-weight:500;font-size:35px;line-height:42px;letter-spacing:1px}
.hero-title b{font-weight:800}
.hero-sub{left:113px;top:356px;width:320px;color:#f3f3f3;font-size:15px;line-height:22px}
.btn{display:inline-block;background:var(--green);color:var(--white);font-size:11px;font-weight:600;text-align:center}
.hero-btn{left:113px;top:427px;width:112px;height:34px;line-height:34px}

/* services ribbon */
.ribbon{left:81px;top:619px;width:1038px;height:205px}
.service{top:668px;width:259px;text-align:center;color:var(--white)}
.service svg{width:50px;height:50px}
.service h4{font-family:"Raleway",sans-serif;font-size:11px;font-weight:700;margin-top:8px;letter-spacing:.4px}
.service p{font-size:9px;opacity:.9;margin-top:3px}

/* how it works */
.section-title{width:1200px;left:0;text-align:center;font-family:"Raleway",sans-serif;font-weight:500;font-size:31px;color:#222}
.how-intro{left:230px;top:935px;width:740px;text-align:center;font-size:13px;line-height:22px;color:#444}
.step{top:1005px;width:260px;text-align:center}
.step svg{width:44px;height:44px}
.step h5{font-family:"Raleway",sans-serif;font-size:15px;font-weight:500;margin-top:18px}
.step p{width:200px;margin:6px auto 0;font-size:10px;line-height:17px;color:var(--muted)}

.programs{left:0;top:1216px;width:1200px;height:225px;background:linear-gradient(90deg,#1aafc0,#22b7c7 50%,#1aafc0)}
.programs-text{left:0;top:1298px;width:1200px;text-align:center;color:var(--white);font-family:"Raleway",sans-serif}
.programs-text small{display:block;font-size:14px;letter-spacing:3px;opacity:.85}
.programs-text span{display:block;font-size:29px;margin-top:4px}

/* recipes */
.recipe{top:1554px;width:330px}
.recipe .photo{width:330px;height:225px}
.recipe h5{width:270px;font-family:"Raleway",sans-serif;font-size:16px;font-weight:600;line-height:24px;margin-top:44px;height:48px}
.recipe p{width:290px;font-size:11px;line-height:18px;color:#555;margin-top:10px}
.recipe .btn{width:65px;height:26px;line-height:26px;font-size:10px;margin-top:22px}

.gallery{left:0;top:2073px;width:1200px;height:387px;display:grid;grid-template-columns:repeat(4,1fr);grid-template-rows:repeat(2,1fr)}
.gallery div{width:100%;height:100%}
.gallery-arrow{right:0;top:2394px;width:26px;height:30px;background:var(--teal);border-radius:15px 0 0 15px}

/* testimonials */
.clients-title{top:2500px;font-size:24px}
.clients-sub{left:400px;top:2546px;width:400px;text-align:center;font-size:10px;line-height:16px;color:#555}
.quote-card{left:200px;top:2608px;width:797px;height:230px;border:1px solid var(--line);background:var(--white);box-shadow:0 1px 4px rgba(0,0,0,.08)}
.quote-mark{left:0;top:20px;width:797px;text-align:center;font-family:"Raleway",sans-serif;font-weight:800;font-size:40px;color:var(--green);line-height:40px}
.quote-text{left:60px;top:64px;width:677px;text-align:center;font-size:11px;line-height:18px;color:#444}
.avatar{left:380px;top:118px;width:38px;height:38px;border-radius:50%;background:linear-gradient(#c7ad9c,#7d675c)}
.quote-name{left:0;top:162px;width:797px;text-align:center;font-family:"Raleway",sans-serif;font-weight:600;font-size:14px}
.quote-role{left:0;top:183px;width:797px;text-align:center;font-size:10px;color:var(--muted)}
.circle-arrow{top:2716px;width:28px;height:28px;border:1px solid var(--green);border-radius:50%;background:var(--white)}

/* subscribe */
.subscribe{left:0;top:2887px;width:1200px;height:186px;background:linear-gradient(90deg,#82bd3a,#92ca47 50%,#86c03d)}
.subscribe-title{left:0;top:2942px;width:1200px;text-align:center;font-family:"Raleway",sans-serif;font-weight:500;font-size:24px;color:var(--white);letter-spacing:.5px}
.subscribe-form{left:283px;top:2985px;width:636px;height:37px;display:flex;background:var(--white);border-radius:18px;overflow:hidden}
.subscribe-form span{flex:1;font-size:11px;line-height:37px;padding-left:16px;color:#333;border-right:1px solid #ccc}
.subscribe-form b{width:110px;font-size:11px;font-weight:600;line-height:37px;text-align:center}

.map{left:0;top:3073px;width:1200px;height:403px;
  background:
    radial-gradient(ellipse 260px 160px at 870px 190px,rgba(170,205,225,.55),rgba(170,205,225,0)),
    radial-gradient(ellipse 300px 200px at 300px 250px,rgba(205,225,190,.6),rgba(205,225,190,0)),
    linear-gradient(160deg,#eceee8,#e4e9dd 50%,#dde6e4)}
.map-pin{left:588px;top:3245px;width:24px;height:34px}

/* contacts */
.contact-box{top:3476px;width:400px;height:254px;color:var(--white);text-align:center}
.contact-box svg{margin-top:70px;width:26px;height:26px}
.contact-box p{font-size:15px;margin-top:38px}
.contact-box small{display:block;font-size:9px;letter-spacing:2px;margin-top:18px;opacity:.85}

/* footer */
.footer{left:0;top:3730px;width:1200px;height:324px;background:var(--navy)}
.footer-logo{left:0;top:3835px;width:1200px;text-align:center;font-family:"Raleway",sans-serif;font-weight:800;font-size:40px;color:var(--green);letter-spacing:1px}
.footer-nav{left:0;top:3932px;width:1200px;display:flex;justify-content:center;gap:22px;font-size:9px;color:#cfd3da;letter-spacing:1px}
.footer-social{left:0;top:3986px;width:1200px;display:flex;justify-content:center;gap:42px}
.footer-social i{display:block;width:16px;height:16px;border-radius:50%;background:var(--white)}
</style>
</head>
<body>

<!-- Hero -->
<div class="abs hero" role="img" aria-label="Smiling woman leaning on a kitchen counter beside fresh vegetables"></div>

<div class="abs topbar">
  <div class="abs links"><span>Links &amp; Resources</span><span>|</span><span>Success Stories</span></div>
  <div class="abs social"><i></i><i></i><i></i><i></i><i></i><i></i></div>
</div>

<header class="abs header">
  <div class="abs logo"><i></i>BRIGHTPATH</div>

  <div class="abs contact-item" style="left:410px">
    <svg viewBox="0 0 24 24" fill="none" stroke="#8cc63e" stroke-width="1.8"><path d="M5 3h4l2 5-3 2a11 11 0 0 0 6 6l2-3 5 2v4a2 2 0 0 1-2 2A17 17 0 0 1 3 5a2 2 0 0 1 2-2z"/></svg>
    <div><small>We're on call 24/7</small><b>+1 555 210 4478</b></div>
  </div>
  <div class="abs contact-item" style="left:615px">
    <svg viewBox="0 0 24 24" fill="none" stroke="#8cc63e" stroke-width="1.8"><circle cx="12" cy="12" r="9"/><path d="M12 7v5l3 2"/></svg>
    <div><small>Operating Hours</small><b>Mon – Fri 08.00 – 20.00</b></div>
  </div>
  <div class="abs contact-item" style="left:820px">
    <svg viewBox="0 0 24 24" fill="none" stroke="#8cc63e" stroke-width="1.8"><rect x="3" y="6" width="18" height="13"/><path d="M3 6l9 7 9-7"/></svg>
    <div><small>Get in touch</small><b>hello@brightpathmoments.net</b></div>
  </div>

  <nav class="abs nav"><span>Home</span><span>About</span><span>Work with me</span><span>Success stories</span><span>Blog</span><span>Connect</span><span>More</span></nav>
</header>

<h1 class="abs hero-title">ARE YOU READY TO<br><b>TRANSFORM YOUR LIFE?</b></h1>
<p class="abs hero-sub">Most people have no idea how good their body is designed to feel</p>
<span class="abs btn hero-btn">Click here</span>

<!-- Services ribbon -->
<svg class="abs ribbon" viewBox="0 0 1038 205" preserveAspectRatio="none">
  <polygon points="0,14 259,14 259,190 130,176 0,190" fill="#92c943"/>
  <polygon points="259,0 519,0 519,205 389,190 259,205" fill="#86c03a"/>
  <polygon points="519,14 779,14 779,190 649,176 519,190" fill="#92c943"/>
  <polygon points="779,0 1038,0 1038,205 908,190 779,205" fill="#86c03a"/>
  <polygon points="259,0 259,14 250,14" fill="#6da22a"/>
  <polygon points="519,0 519,14 528,14" fill="#6da22a"/>
  <polygon points="779,0 779,14 770,14" fill="#6da22a"/>
</svg>
<div class="abs service" style="left:81px">
  <svg viewBox="0 0 50 50" fill="none" stroke="#fff" stroke-width="2"><circle cx="25" cy="25" r="18"/><path d="M25 34l-8-8a5 5 0 0 1 8-6 5 5 0 0 1 8 6z"/></svg>
  <h4>CHANGE SERVICES</h4><p>Work with me</p>
</div>
<div class="abs service" style="left:340px">
  <svg viewBox="0 0 50 50" fill="none" stroke="#fff" stroke-width="2"><circle cx="25" cy="12" r="5"/><path d="M25 18v12M12 26l13 4 13-4M14 40l11-10 11 10M10 42h30"/></svg>
  <h4>HOLISTIC APPROACH</h4><p>Meet my associates</p>
</div>
<div class="abs service" style="left:600px">
  <svg viewBox="0 0 50 50" fill="none" stroke="#fff" stroke-width="2"><path d="M8 40l12-16 8 10 6-7 8 13z"/><circle cx="36" cy="12" r="4"/><path d="M36 3v3M36 18v3M27 12h3M42 12h3"/></svg>
  <h4>SUCCESS STORIES</h4><p>Get inspired &amp; motivated</p>
</div>
<div class="abs service" style="left:860px">
  <svg viewBox="0 0 50 50" fill="none" stroke="#fff" stroke-width="2"><rect x="8" y="10" width="34" height="32"/><path d="M8 18h34M16 6v8M34 6v8M15 25h4M23 25h4M31 25h4M15 33h4M23 33h4"/></svg>
  <h4>REQUEST AN APPOINTMENT</h4><p>Call me or fill in a form</p>
</div>

<!-- How it works -->
<h2 class="abs section-title" style="top:872px">How it works?</h2>
<p class="abs how-intro">Organizations regulating organic products may choose to restrict the use of certain pesticides and fertilizers in farming.<br>In general, irradiation, industrial solvents or synthetic food additives.</p>

<div class="abs step" style="left:175px">
  <svg viewBox="0 0 46 46" fill="none" stroke="#8cc63e" stroke-width="2"><path d="M6 22h34a17 17 0 0 1-34 0zM16 22c0-6 6-8 6-14M26 22c0-4 4-6 8-8"/></svg>
  <h5>Eat healthy</h5>
  <p>Eating habits should be regulated and controlled – only natural organic food will make our body healthy and strong.</p>
</div>
<div class="abs step" style="left:470px">
  <svg viewBox="0 0 46 46" fill="none" stroke="#8cc63e" stroke-width="2"><circle cx="11" cy="30" r="8"/><circle cx="35" cy="30" r="8"/><path d="M11 30l8-12h12l4 12M19 18l5 12h-13M26 14h6"/></svg>
  <h5>Workout hard</h5>
  <p>Diet is not the only ingredient of a long happy life. Physical exercise is also important for your health and beauty.</p>
</div>
<div class="abs step" style="left:765px">
  <svg viewBox="0 0 46 46" fill="none" stroke="#8cc63e" stroke-width="2"><path d="M8 20h8v20H8zM16 22l7-14c4 0 4 4 3 9h12a3 3 0 0 1 2 4l-4 15a3 3 0 0 1-3 2H16"/></svg>
  <h5>Enjoy your life</h5>
  <p>See how your life becomes a pleasant adventure full of bright colors and fun activities. Meet new friends as well.</p>
</div>

<!-- Programs -->
<div class="abs programs" role="img" aria-label="Faint photo band of smiling people over teal"></div>
<div class="abs programs-text"><small>OUR PROGRAMS</small><span>Our Qualifications</span></div>

<!-- Recipes -->
<h2 class="abs section-title" style="top:1485px">Healthy Recipes</h2>
<div class="abs recipe" style="left:81px">
  <div class="photo" role="img" aria-label="Pizza topped with tomatoes and mozzarella" style="background:linear-gradient(160deg,#5d3a22,#a94a2c 50%,#c98c4e)"></div>
  <h5>Lavash Pizza with Tomatoes and Mozzarella</h5>
  <p>Lorem ipsum dolor sit amet, in duo wisi meis brute, mei ferri conceptam non debet omittamulla ocurreret pero.</p>
  <span class="btn">Read More</span>
</div>
<div class="abs recipe" style="left:435px">
  <div class="photo" role="img" aria-label="Grilled chicken salad with avocado and tomatoes" style="background:linear-gradient(160deg,#8f8a7f,#9bb662 50%,#d8c8a8)"></div>
  <h5>Chicken Salad with Tomatoes and Avocado</h5>
  <p>Lorem ipsum dolor sit amet, in duo wisi meis brute, mei ferri conceptam non debet omittamulla ocurreret pero.</p>
  <span class="btn">Read More</span>
</div>
<div class="abs recipe" style="left:789px">
  <div class="photo" role="img" aria-label="Salted salmon fillet with parmesan and potatoes" style="background:linear-gradient(160deg,#4a5a45,#d9714c 50%,#e9a07d)"></div>
  <h5>Salted Salmon with Parmesan and Potatoes</h5>
  <p>Lorem ipsum dolor sit amet, in duo wisi meis brute, mei ferri conceptam non debet omittamulla ocurreret pero.</p>
  <span class="btn">Read More</span>
</div>

<!-- Gallery -->
<div class="abs gallery">
  <div role="img" aria-label="Measuring tape around a waist" style="background:linear-gradient(160deg,#d6c2b4,#b49a88)"></div>
  <div role="img" aria-label="Person holding fresh fruit" style="background:linear-gradient(160deg,#ecece6,#c3d49c)"></div>
  <div role="img" aria-label="Running shoes on a treadmill" style="background:linear-gradient(160deg,#8a8a8c,#5f5f63)"></div>
  <div role="img" aria-label="Group of women in workout clothes" style="background:linear-gradient(160deg,#e7e4e6,#d49ab3)"></div>
  <div role="img" aria-label="Man lifting dumbbells" style="background:linear-gradient(160deg,#7c8a98,#4b6e98)"></div>
  <div role="img" aria-label="Breakfast with juice, fruit and cereal" style="background:linear-gradient(160deg,#f3e6cf,#e7b46a)"></div>
  <div role="img" aria-label="Hands preparing vegetables" style="background:linear-gradient(160deg,#cfc8bc,#93a66c)"></div>
  <div role="img" aria-label="Bowl of oatmeal with berries" style="background:linear-gradient(160deg,#e7ddd0,#c9a184)"></div>
</div>
<div class="abs gallery-arrow"></div>

<!-- Testimonials -->
<h2 class="abs section-title clients-title">OUR CLIENTS SAY</h2>
<p class="abs clients-sub">Lorem ipsum dolor sit amet consectetur adipiscing elitsed eiusmod tempor anim minim veniam quis nulla exercit</p>
<div class="abs quote-card">
  <div class="abs quote-mark">&ldquo;</div>
  <p class="abs quote-text">Lorem Ipsum is simply dummy text of the printing and typesetting industry. Lorem Ipsum has been the industry's standard dummy text ever since the 1500s, when an unknown printer took a galley of type and scrambled it to make a type specimen book.</p>
  <div class="abs avatar" role="img" aria-label="Client portrait"></div>
  <div class="abs quote-name">Dana Merrit</div>
  <div class="abs quote-role">CEO – Company Name</div>
</div>
<svg class="abs circle-arrow" style="left:210px" viewBox="0 0 28 28" fill="none" stroke="#8cc63e" stroke-width="2"><path d="M16 9l-5 5 5 5"/></svg>
<svg class="abs circle-arrow" style="left:954px" viewBox="0 0 28 28" fill="none" stroke="#8cc63e" stroke-width="2"><path d="M12 9l5 5-5 5"/></svg>

<!-- Subscribe -->
<div class="abs subscribe" role="img" aria-label="Faint photo of a runner over green"></div>
<h3 class="abs subscribe-title">SUBSCRIBE &amp; GET AMAZING UPDATE</h3>
<div class="abs subscribe-form"><span>Enter your email</span><b>SUBSCRIBE</b></div>

<!-- Map -->
<div class="abs map" role="img" aria-label="Road map of the surrounding region with lakes and towns"></div>
<svg class="abs map-pin" viewBox="0 0 24 34"><path d="M12 0a11 11 0 0 1 11 11c0 8-11 23-11 23S1 19 1 11A11 11 0 0 1 12 0z" fill="#222"/><circle cx="12" cy="11" r="4" fill="#fff"/></svg>

<!-- Contact boxes -->
<div class="abs contact-box" style="left:0;background:var(--orange)">
  <svg viewBox="0 0 26 26" fill="none" stroke="#fff" stroke-width="1.8"><rect x="7" y="2" width="12" height="22" rx="2"/><path d="M11 20h4"/></svg>
  <p>1-800-555-0142</p><small>PHONE</small>
</div>
<div class="abs contact-box" style="left:400px;background:var(--green)">
  <svg viewBox="0 0 26 26" fill="none" stroke="#fff" stroke-width="1.8"><path d="M13 2a8 8 0 0 1 8 8c0 6-8 14-8 14S5 16 5 10a8 8 0 0 1 8-8z"/><circle cx="13" cy="10" r="3"/></svg>
  <p>Marlow, OR 97204, United States</p><small>ADDRESS</small>
</div>
<div class="abs contact-box" style="left:800px;background:var(--teal)">
  <svg viewBox="0 0 26 26" fill="none" stroke="#fff" stroke-width="1.8"><rect x="2" y="6" width="22" height="15"/><path d="M2 6l11 8 11-8"/></svg>
  <p>team@brightpathmoments.net</p><small>EMAIL</small>
</div>

<!-- Footer -->
<footer class="abs footer"></footer>
<div class="abs footer-logo">BRIGHTPATH</div>
<nav class="abs footer-nav"><span>HOME</span><span>|</span><span>ABOUT</span><span>|</span><span>CLASSES</span><span>|</span><span>BLOG</span><span>|</span><span>SHOP</span><span>|</span><span>CONTACTS</span></nav>
<div class="abs footer-social"><i></i><i></i><i></i><i></i><i></i></div>

</body>
</html>
```